Etikett für Likörflasche - Moonshine
Zielgruppe
Wir sind eine kleine Moonshine / Likörmanufaktur. Unser Obst für die Brände und Liköre stammt aus eigenem Anbau bzw. von umliegenden regionalen Bauern. Hier setzen wir auf sehr gute Qualität und verwenden keine Zusatzstoffe, Geschmacksverstärker, Farbstoffe etc. Im ersten Schritt werden wir nur 3-4 verschiedene Liköre anbieten.
Wir möchten unsere Liköre zukünftig auf Veranstaltungen / Events und Märkten verkaufen. Hierfür suchen wir ein pfiffiges und ansprechendes Etikettendesign.
Das Wort 'Moonshine' soll die Leute auf den Events zu uns führen. Das wird auch mit großen Fahnen am Verkaufsstand beworben. Da wir auch ein paar amerikanische Foodtrucks haben soll auch das Etikett ein bisschen amerikanisch gehalten werden.
Zielgruppe: 28 bis 55 Jahre (Männer & Frauen)
Verkaufspreis pro 0,5 Liter Flasche ca. 24,50 Euro
Aufgabenstellung
Es soll ein Etikett auf die Flasche (nur vorne nicht auf die Rückseite).
Etikettengröße: ca. 7,0 x 8,5cm (für die 0,5l Flasche)
Angaben die sich auf dem Etikett ändern:
- Inhalt entweder 0,35l oder 0,5l Flasche
- Bezeichnung vom Inhalt und 'Kurzbeschreibung'
- Alkoholgehalt
Ich habe in PowerPoint schon mal ein Etikett zusammen gestellt, auf dem die Angaben alle mit enthalten sind. Hier fehlt mir allerdings der Pfiff und das Professionelle. Auch die Darstellung der Eigenschaften wie 'Echte Früchte', 'Handcrafted' etc. gefällt mir so auch nicht. Vielleicht wäre auch noch ein cooler Spruch darauf gut.
In die Anlage habe ich meine kreierte PowerPoint Folie gepackt (auf der 2. Folie findet ihr die geplante Flasche in die abgefüllt wird). Die zweite Datei ist ein Design was meinen Vorstellungen schon gut nahe kommt aus dem Internet (hier gefallen mir die Linien, kleine Gimmicks etc. da passiert einfach was auf dem Etikett). Von der Art her würde mir dieser Style gut gefallen. Es soll nur nicht zu überladen und kitschig werden.
Likörsorten die es geben wird: Wir werden uns erstmal auf 3-4 Sorten beschränken.

```html
<!DOCTYPE html>
<html lang="de">
<head>
<meta charset="utf-8">
<title>Marten's Moonshine – Mossy &amp; Berry Etikett</title>
<link rel="stylesheet" href="https://fonts.googleapis.com/css2?family=Bebas+Neue&family=Bitter:ital,wght@0,400;0,800;1,400&display=swap">
<style>
  :root {
    --paper: #f3f2f0;
    --gold: #b08d4f;
    --gold-soft: #cdb486;
    --moon-light: #ece4d2;
    --moon-dark: #d6c6a2;
    --ink: #141414;
    --white: #fbfbfa;
  }
  html, body {
    margin: 0;
    padding: 0;
    width: 1200px;
    height: 1200px;
    overflow: hidden;
    background: var(--paper);
  }
  .label { display: block; width: 1200px; height: 1200px; }
  .display { font-family: "Bebas Neue", "Impact", sans-serif; fill: var(--ink); }
  .slab { font-family: "Bitter", Georgia, serif; font-weight: 800; fill: var(--ink); }
  .body-serif { font-family: "Bitter", Georgia, serif; font-weight: 400; fill: var(--ink); }
  .tasting-note { font-family: "Bitter", Georgia, serif; font-style: italic; font-size: 25px; fill: var(--ink); }
  .frame-line { fill: none; stroke: var(--gold); stroke-width: 4; }
  .frame-line-thin { fill: none; stroke: var(--gold); stroke-width: 2.5; }
  .band-fill { fill: var(--gold-soft); }
  .box-white { fill: var(--white); stroke: var(--gold); stroke-width: 3.5; }
</style>
</head>
<body>
<svg class="label" viewBox="0 0 1200 1200" xmlns="http://www.w3.org/2000/svg">
  <defs>
    <radialGradient id="moonTone" cx="0.45" cy="0.4" r="0.65">
      <stop offset="0" stop-color="var(--moon-light)"/>
      <stop offset="1" stop-color="var(--moon-dark)"/>
    </radialGradient>
  </defs>

  <!-- outer frame -->
  <g class="outer-frame">
    <rect class="frame-line" x="172" y="88" width="858" height="1034" rx="10"/>
    <rect class="frame-line-thin" x="182" y="98" width="838" height="1014" rx="6"/>
  </g>

  <!-- full moon area -->
  <circle class="moon" cx="617" cy="511" r="438" fill="url(#moonTone)" stroke="var(--gold)" stroke-width="4"
          role="img" aria-label="Foto des Vollmonds hinter dem Schriftzug"/>

  <!-- brand lockup -->
  <g class="brand">
    <text class="display tagline-top" x="200" y="238" font-size="84" transform="rotate(-4 200 238)">THE FAMOUS</text>
    <text class="display brand-name" x="148" y="395" font-size="165" textLength="430" lengthAdjust="spacingAndGlyphs">MARTEN'S</text>
    <text class="slab tagline-years" x="632" y="318" font-size="27" transform="rotate(-6 632 318)">100 YEARS OF EXPERIENCE</text>
    <text class="display brand-name" x="138" y="622" font-size="235" textLength="932" lengthAdjust="spacingAndGlyphs">MOONSHINE</text>
  </g>

  <!-- product band -->
  <g class="product-band">
    <rect class="band-fill" x="140" y="672" width="932" height="197" rx="98" stroke="var(--gold)" stroke-width="4"/>
    <rect class="frame-line-thin" x="150" y="682" width="912" height="177" rx="88" fill="none"/>
    <rect class="box-white" x="159" y="692" width="891" height="158"/>
    <rect class="frame-line-thin" x="167" y="700" width="875" height="142" fill="none"/>
    <rect class="box-white" x="475" y="640" width="259" height="50" rx="18"/>
    <text class="slab" x="604.5" y="678" font-size="26" text-anchor="middle">THE ONE &amp; ONLY</text>
    <text class="display product-name" x="604.5" y="830" font-size="162" text-anchor="middle" textLength="790" lengthAdjust="spacingAndGlyphs">MOSSY &amp; BERRY</text>
  </g>

  <!-- lower info panel -->
  <g class="info-panel">
    <rect class="band-fill" x="182" y="850" width="838" height="218"/>
    <rect class="frame-line-thin" x="182" y="850" width="838" height="218" fill="none"/>

    <path class="box-white" d="M181 838 H425 V1006 H241 a60 60 0 0 1 -60 -60 Z"/>
    <path class="box-white" d="M781 838 H1020 V946 a60 60 0 0 1 -60 60 H781 Z"/>
    <rect class="box-white" x="428" y="856" width="350" height="184" rx="18"/>

    <text class="slab" x="298" y="911" font-size="18" text-anchor="middle">AUTHENTIC TASTE</text>
    <text class="slab" x="298" y="942" font-size="18" text-anchor="middle">SEASONED WITH</text>
    <text class="slab" x="298" y="962" font-size="18" text-anchor="middle">FRUITS</text>

    <text class="tasting-note" x="603" y="938" text-anchor="middle">Wilde Beeren treffen auf</text>
    <text class="tasting-note" x="603" y="968" text-anchor="middle">vielschichtige Noten</text>
    <text class="tasting-note" x="603" y="998" text-anchor="middle">von Whiskey und Karamell</text>

    <text class="slab" x="900" y="920" font-size="18" text-anchor="middle">100% HANDCRAFTED</text>
    <text class="slab" x="900" y="952" font-size="18" text-anchor="middle">NO ADDITIVES</text>

    <rect class="box-white" x="544" y="840" width="118" height="63" rx="26"/>
    <text class="slab" x="603" y="867" font-size="18" text-anchor="middle">22% Vol</text>
    <text class="slab" x="603" y="888" font-size="18" text-anchor="middle">44 Proof</text>

    <rect class="box-white" x="560" y="1034" width="88" height="38"/>
    <text class="slab" x="604" y="1061" font-size="20" text-anchor="middle">500ml</text>
  </g>

  <!-- footer address -->
  <g class="footer">
    <rect class="box-white" x="182" y="1078" width="838" height="34" stroke-width="0"/>
    <text class="body-serif" x="601" y="1102" font-size="17" text-anchor="middle">Marten's Moonshine – Am Lindenhang 12 – 90412 Talbach – <tspan font-weight="800">www.martens-moonshine.de</tspan></text>
  </g>
</svg>
</body>
</html>
```